Looking for a creative label design for our retail coffee bags

We are a coffee manufacturer (coffee roaster) looking to re-brand our retail label for our coffee bags. Our main coffee blend that we sell is our Colombian Supremo Blend. You can use this name when creating the label. We are going for a look that represents our company as a coffee roaster. Please reference our website (www.brindlemoorroasters.com) and our Facebook page to learn more about our company and to give you more inspiration on creating this design.

Target Market(s)

Retail customers/grocery stores

Industry/Entity Type

Manufacturer

Requirements
Must have
• The size of the label has to be 3" width x 4" height

Logo must be Black
Nice to have
• We currently incorporate a color on our labels for each blend. For example, Colombian Supremo Blend (royal blue), Decaffeinated Blend (red), Breakfast Blend (green), Flavored coffees (gold).

Rustic/vintage style

```html
<!DOCTYPE html>
<html lang="en">
<head>
<meta charset="utf-8">
<title>Brindlemoor Roasters – Colombian Supremo Blend Label</title>
<link rel="stylesheet" href="https://fonts.googleapis.com/css2?family=Archivo+Black&display=swap">
<style>
  :root {
    --label-white: #ffffff;
    --ink-black: #000000;
    --blend-royal-blue: #0f10c4;
  }
  * { margin: 0; padding: 0; box-sizing: border-box; }
  html, body {
    width: 900px;
    height: 1200px;
    overflow: hidden;
    background: var(--label-white);
  }
  .label {
    position: relative;
    width: 900px;
    height: 1200px;
    background: var(--label-white);
    font-family: "Archivo Black", "Arial Black", sans-serif;
  }
  .brand-name {
    position: absolute;
    left: 0;
    top: 40px;
    width: 900px;
    height: 760px;
    display: flex;
    flex-direction: column;
    align-items: center;
    justify-content: center;
    color: var(--ink-black);
    font-size: 104px;
    line-height: 1.1;
    text-align: center;
    letter-spacing: 1px;
  }
  .blend-band {
    position: absolute;
    left: 39px;
    top: 825px;
    width: 822px;
    height: 253px;
    background: var(--blend-royal-blue);
    display: flex;
    flex-direction: column;
    align-items: center;
    justify-content: center;
    text-align: center;
  }
  .blend-origin,
  .blend-type {
    color: var(--ink-black);
    -webkit-text-stroke: 8px var(--label-white);
    paint-order: stroke fill;
    white-space: nowrap;
  }
  .blend-origin {
    font-size: 122px;
    line-height: 1;
    letter-spacing: -3px;
    margin-top: -12px;
  }
  .blend-type {
    font-size: 50px;
    line-height: 1;
    letter-spacing: 1px;
    margin-top: 18px;
    -webkit-text-stroke: 6px var(--label-white);
  }
</style>
</head>
<body>
  <main class="label">
    <h1 class="brand-name">
      <span>Brindlemoor</span>
      <span>Roasters</span>
    </h1>
    <section class="blend-band">
      <p class="blend-origin">Colombian</p>
      <p class="blend-type">SUPREMO BLEND</p>
    </section>
  </main>
</body>
</html>
```